Harborvale Ventures brochure for Investment partnership, young harold pembly

We need a brochure design to attract new investors for our investing partnership Called Harborvale Ventures. We are based in New Orleans, La. We primarily invest in stocks, bonds, and crypto but venture out into other categories as well. We would like to see designs with the black and gold like our logo. The final design should say new, fresh, sleek, tech, and honorable. BROUCHURE WILL BE 4 pages.or one folded sheet a paparer if that makes sense.
Updates

A chart showing Harborvale Ventures gains since 2019 28.6 percent and the TR 400 gAINS 7.1 PERCENT

Target Market(s)

Probable Investors

Industry/Entity Type

Financial Planning

Colors

Designer to choose only greyscale colors for use in the design.

Requirements
Must have
• Black and Gold accent. Stock market feel. Sleek, High tech, innovative, Intellgent design.
Nice to have
• Page colors possibly black.
Should not have
• Boring, Old school,

```html
<!DOCTYPE html>
<html lang="en">
<head>
<meta charset="utf-8">
<title>Harborvale Ventures Brochure</title>
<link href="https://fonts.googleapis.com/css2?family=Cinzel:wght@700&family=Montserrat:ital,wght@0,400;0,500;0,700;1,700&display=swap" rel="stylesheet">
<style>
  :root {
    --backdrop: #e3e3e6;
    --page: #0e0e0e;
    --page-deep: #070707;
    --gold: #d9b92c;
    --gold-band: #e3c12b;
    --ink-light: #e9e9e9;
    --ink-muted: #b9b9b9;
    --photo-light: #bdbdbd;
    --photo-dark: #2a2a2a;
  }
  * { box-sizing: border-box; margin: 0; padding: 0; }
  html, body { width: 1200px; height: 2700px; overflow: hidden; }
  body { background: var(--backdrop); position: relative; font-family: "Montserrat", sans-serif; }

  .panel { position: absolute; left: 0; width: 1200px; height: 900px; }
  .panel--cover { top: 0; }
  .panel--outside { top: 900px; }
  .panel--inside { top: 1800px; }

  .page {
    position: absolute; top: 68px; width: 540px; height: 764px;
    background: var(--page); overflow: hidden;
    box-shadow: 0 24px 40px rgba(0,0,0,0.22);
  }
  .page--solo { left: 330px; }
  .page--left { left: 60px; }
  .page--right { left: 600px; }
  .page--left::after {
    content: ""; position: absolute; right: 0; top: 0; width: 18px; height: 100%;
    background: linear-gradient(to left, rgba(255,255,255,0.05), transparent);
  }

  .brand-name {
    position: absolute; font-family: "Cinzel", serif; font-weight: 700;
    color: var(--gold); white-space: nowrap; letter-spacing: 1px;
  }

  /* Front cover */
  .cover__brand { top: 52px; left: 0; width: 100%; text-align: center; font-size: 30px; }
  .cover__rule { position: absolute; top: 98px; left: 150px; width: 240px; height: 1px; background: var(--gold); }
  .cover__photo {
    position: absolute; left: 56px; top: 136px; width: 428px; height: 310px;
    border: 3px solid #e6e6e6;
    background: linear-gradient(160deg, var(--photo-light) 0%, #7a7a7a 35%, var(--photo-dark) 70%, #5c5c5c 100%);
  }
  .cover__headline {
    position: absolute; top: 478px; left: 0; width: 100%; text-align: center;
    font-family: "Cinzel", serif; font-weight: 700; color: var(--gold);
    font-size: 26px; line-height: 30px; letter-spacing: 0.5px;
  }
  .cover__subline {
    position: absolute; top: 546px; left: 0; width: 100%; text-align: center;
    color: var(--ink-light); font-size: 15px; letter-spacing: 1px; font-weight: 500;
  }
  .cover__band {
    position: absolute; top: 584px; left: 60px; width: 420px; height: 34px;
    background: var(--gold-band); color: #111; text-align: center;
    font-weight: 700; font-size: 16px; line-height: 34px; letter-spacing: 1px;
  }
  .cover__web {
    position: absolute; top: 668px; left: 0; width: 100%; text-align: center;
    color: var(--ink-light); font-size: 13px; letter-spacing: 1.5px;
  }
  .cover__web b, .back__web b, .inside__web b { color: var(--gold); font-weight: 400; }

  /* Back cover */
  .back { background: radial-gradient(ellipse at 50% 30%, #1b1b1b 0%, var(--page-deep) 70%); }
  .back__texture {
    position: absolute; left: 0; top: 0; width: 100%; height: 100%;
    background: linear-gradient(180deg, rgba(40,40,40,0.35) 0%, transparent 60%, rgba(25,25,25,0.4) 100%);
  }
  .back__title {
    position: absolute; top: 440px; left: 60px; color: var(--gold);
    font-weight: 700; font-style: italic; font-size: 17px; line-height: 21px;
  }
  .back__body {
    position: absolute; top: 490px; left: 60px; width: 420px;
    color: var(--ink-muted); font-size: 11px; line-height: 15px;
  }
  .back__brand { top: 590px; left: 60px; font-size: 18px; }
  .back__contact {
    position: absolute; left: 60px; color: var(--ink-light); font-size: 12px;
    letter-spacing: 1px; display: flex; align-items: center; gap: 8px;
  }
  .back__phone { top: 638px; }
  .back__web { top: 662px; }
  .back__social { position: absolute; top: 665px; left: 300px; display: flex; gap: 5px; }
  .back__social span { width: 9px; height: 9px; border-radius: 50%; background: var(--ink-light); }

  /* Inside spread */
  .inside__image {
    position: absolute; left: 40px; top: 150px; width: 250px; height: 470px;
    background: radial-gradient(ellipse at 45% 45%, #8a7a55 0%, #4d4330 35%, #1c1a15 65%, var(--page) 100%);
  }
  .inside__intro {
    position: absolute; left: 305px; top: 300px; width: 190px;
    color: var(--ink-light); font-size: 11.5px; line-height: 16px;
  }
  .inside__brand { top: 640px; left: 48px; font-size: 18px; }
  .steps {
    position: absolute; left: 60px; top: 200px; width: 420px; height: 390px;
    border: 1.5px solid var(--gold); padding: 34px 32px;
  }
  .steps__title { color: var(--gold); font-weight: 700; font-size: 15px; margin-bottom: 16px; }
  .steps__list { list-style: none; }
  .steps__item { display: flex; gap: 16px; margin-bottom: 14px; }
  .steps__num { color: var(--gold); font-size: 17px; width: 16px; flex: none; }
  .steps__text { color: var(--ink-light); font-size: 10.5px; line-height: 14px; }
  .inside__web {
    position: absolute; top: 700px; right: 40px; color: var(--ink-light);
    font-size: 13px; letter-spacing: 1.5px; display: flex; align-items: center; gap: 12px;
  }
  .dot { width: 6px; height: 6px; border-radius: 50%; background: var(--gold); }
</style>
</head>
<body>

<!-- Panel 1: front cover -->
<section class="panel panel--cover">
  <article class="page page--solo cover">
    <div class="brand-name cover__brand">Harborvale Ventures</div>
    <div class="cover__rule"></div>
    <div class="cover__photo" role="img" aria-label="Black and white photo of a historic streetcar on a palm-lined city avenue"></div>
    <h1 class="cover__headline">Become a Partner and<br>Build Generational Wealth</h1>
    <p class="cover__subline">BY INVESTING IN THE STOCK MARKET</p>
    <div class="cover__band">A FIRST OF ITS KIND INVESTMENT</div>
    <p class="cover__web">www.<b>harborvaleventures</b>.com</p>
  </article>
</section>

<!-- Panel 2: outside spread -->
<section class="panel panel--outside">
  <article class="page page--left back">
    <div class="back__texture" role="img" aria-label="Faint dark background photo of a city street"></div>
    <h2 class="back__title">About Harborvale Ventures<br>and General Partner</h2>
    <p class="back__body">Harborvale Ventures was founded in 2019 by General Partner Dorian Maddox Jr with a group economic empowerment mission. Dorian Maddox has invested in stocks since a teenager, received his BA in economics from Bayou State University and is currently attending Gulf Coast University.</p>
    <div class="brand-name back__brand">Harborvale Ventures</div>
    <p class="back__contact back__phone">
      <svg width="11" height="11" viewBox="0 0 24 24" aria-hidden="true"><path fill="#d9b92c" d="M6.6 10.8a15 15 0 0 0 6.6 6.6l2.2-2.2a1 1 0 0 1 1-.25 11 11 0 0 0 3.6.6 1 1 0 0 1 1 1V20a1 1 0 0 1-1 1A17 17 0 0 1 3 4a1 1 0 0 1 1-1h3.5a1 1 0 0 1 1 1 11 11 0 0 0 .6 3.6 1 1 0 0 1-.25 1z"/></svg>
      012.555.0190
    </p>
    <p class="back__contact back__web"><span class="dot"></span>www.<b>harborvaleventures</b>.com</p>
    <div class="back__social" aria-hidden="true"><span></span><span></span><span></span></div>
  </article>

  <article class="page page--right cover">
    <div class="brand-name cover__brand">Harborvale Ventures</div>
    <div class="cover__rule"></div>
    <div class="cover__photo" role="img" aria-label="Black and white photo of a historic streetcar on a palm-lined city avenue"></div>
    <h1 class="cover__headline">Become a Partner and<br>Build Generational Wealth</h1>
    <p class="cover__subline">BY INVESTING IN THE STOCK MARKET</p>
    <div class="cover__band">A FIRST OF ITS KIND INVESTMENT</div>
    <p class="cover__web">www.<b>harborvaleventures</b>.com</p>
  </article>
</section>

<!-- Panel 3: inside spread -->
<section class="panel panel--inside">
  <article class="page page--left inside">
    <div class="inside__image" role="img" aria-label="Glass jar of coins with a green sprout growing from it beside stacks of coins"></div>
    <p class="inside__intro">If you are receiving this brochure it is because someone sees in you a person that wants to build generational wealth. Not just wealth, but a lasting legacy, using the greatest wealth tool available: the stock market.</p>
    <div class="brand-name inside__brand">Harborvale Ventures</div>
  </article>

  <article class="page page--right inside">
    <div class="steps">
      <h2 class="steps__title">How it works</h2>
      <ol class="steps__list">
        <li class="steps__item"><span class="steps__num">1.</span><span class="steps__text">Make initial deposit. The general partner will invest in stocks, bonds and other investment vehicles on your behalf.</span></li>
        <li class="steps__item"><span class="steps__num">2.</span><span class="steps__text">There is no upfront fees. The general partner will guarantee a 5 percent return and will work for free on your behalf until that is achieved. After the 5 percent return on the dollars invested the limited partner will receive 80 percent and the general partner will receive 20 percent of every dollar gained.</span></li>
        <li class="steps__item"><span class="steps__num">3.</span><span class="steps__text">As the return and investments multiply the interests begin to compound annually. The legal partner legally owns shares of stock within the club and may redeem once a year or let money continue to earn interest.</span></li>
      </ol>
    </div>
    <p class="inside__web"><span class="dot"></span>www.<b>harborvaleventures</b>.com</p>
  </article>
</section>

</body>
</html>
```